Podcast cover art for Steady Footing Podcast for Busy Mothers

I am relaunching my 3 year podcast under a new name. The podcast is called Steady Footing for Busy Mothers. The parent company is called Bright Path Living (see attached logo) and should be represented on the cover in a small way. Previously the show was called Bright Path Living. We talk about creating life balance for working moms by focusing on faith, marriage, parenting, career, health, home, finances, and friends/fun. I don't mind having stock photography on the cover but I prefer not to have my image on it as it is not a personal brand. I have attached a couple of stock images as inspiration.

Target Market(s)

working Christian moms age 30-45 income 75,000+, working full time, Christian faith, married

Industry/Entity Type

Media

Font styles to use
Serif

Requirements
Must have
• Podcast name: Steady Footing for Busy Mothers
• By: Bright Path Living (include logo)
• I also included my brand sheet for reference which includes my brand colors and fonts. Navy should be the primary with orange and gray as the accents
Should not have
• No flowers, or overly girly. My brand is more clean, preppy, and young-sophisticated.

```html
<!DOCTYPE html>
<html lang="en">
<head>
<meta charset="utf-8">
<title>Steady Footing for Busy Mothers — Podcast Cover</title>
<link rel="stylesheet" href="https://fonts.googleapis.com/css2?family=Jost:wght@300;400&display=swap">
<style>
  :root {
    --paper: #ffffff;
    --navy: #272b38;
    --ink: #050505;
    --stone: #b3aeab;
    --orange: #e97a37;
    --white: #ffffff;
    --rule: #1c1c1c;
  }
  html, body {
    margin: 0;
    padding: 0;
    overflow: hidden;
    background: var(--paper);
  }
  .cover {
    position: relative;
    width: 1200px;
    height: 1200px;
    overflow: hidden;
    background: var(--paper);
    font-family: "Jost", "Helvetica Neue", sans-serif;
    font-weight: 300;
  }
  .photo-circle {
    position: absolute;
    left: 0;
    top: 0;
    width: 1200px;
    height: 1200px;
  }
  .divider {
    position: absolute;
    left: 745px;
    top: 132px;
    width: 1.5px;
    height: 784px;
    background: var(--rule);
  }
  .title-block {
    position: absolute;
    display: flex;
    align-items: center;
    height: 125px;
    box-sizing: border-box;
    white-space: nowrap;
    line-height: 1;
  }
  .title-block--lead {
    left: 520px; top: 204px;
    padding: 0 30px 0 36px;
    background: var(--navy);
    color: var(--white);
    font-size: 84px;
    letter-spacing: 2px;
  }
  .title-block--key {
    left: 413px; top: 328px;
    padding: 0 44px 0 38px;
    background: var(--ink);
    color: var(--orange);
    font-size: 110px;
  }
  .title-block--link {
    left: 648px; top: 453px;
    padding: 0 34px 0 34px;
    background: var(--stone);
    color: var(--navy);
    font-size: 84px;
    letter-spacing: 2px;
  }
  .title-block--who {
    left: 610px; top: 578px;
    padding: 0 48px 0 40px;
    background: var(--navy);
    color: var(--white);
    font-size: 110px;
  }
  .title-block--audience {
    left: 478px; top: 703px;
    padding: 0 40px 0 50px;
    background: var(--navy);
    color: var(--orange);
    font-size: 110px;
  }
  .publisher {
    position: absolute;
    left: 744px;
    top: 1050px;
    transform: translateX(-50%);
    display: flex;
    align-items: center;
    gap: 14px;
    white-space: nowrap;
    font-size: 46px;
    font-weight: 300;
    color: var(--ink);
    letter-spacing: 1px;
  }
  .publisher__dot {
    width: 16px;
    height: 16px;
    border-radius: 50%;
    background: var(--ink);
  }
</style>
</head>
<body>
<main class="cover">
  <svg class="photo-circle" viewBox="0 0 1200 1200" xmlns="http://www.w3.org/2000/svg">
    <defs>
      <linearGradient id="photoTones" x1="0" y1="0" x2="1" y2="1">
        <stop offset="0" stop-color="#e4e3e5"/>
        <stop offset="0.35" stop-color="#b9b7b8"/>
        <stop offset="0.6" stop-color="#2a3347"/>
        <stop offset="1" stop-color="#1d2436"/>
      </linearGradient>
    </defs>
    <circle cx="216" cy="600" r="542" fill="var(--orange)"/>
    <circle cx="216" cy="600" r="524" fill="url(#photoTones)" role="img"
            aria-label="Photo: a mother in dark jeans relaxing while holding a smartphone showing a podcast app menu"/>
  </svg>

  <div class="divider"></div>

  <h1 class="podcast-title">
    <span class="title-block title-block--lead">Steady</span>
    <span class="title-block title-block--key">FOOTING</span>
    <span class="title-block title-block--link">for</span>
    <span class="title-block title-block--who">BUSY</span>
    <span class="title-block title-block--audience">MOTHERS</span>
  </h1>

  <div class="publisher">
    <span class="publisher__dot"></span>
    <span class="publisher__name">Bright Path Living</span>
  </div>
</main>
</body>
</html>
```